HiItsJonBrell.com needs a modern, eye-catching business card design

My name is Jon Brell and I own a video training (software development industry) website. I need a business card design that is eye catching for when I travel to conferences or do seminars. I would prefer something simple but bold. Something along the lines of this: https://pixvaultstatic.example/gallery_img/530172/44018/44018_9917302_530172_image.jpg

Note that I do not have a specific logo, but I do have an caricature I use on my site of myself. I've not attached it because I'm not really a fan of having it on my business cards. I would prefer lettering instead of an image. You can go to my website (https://hiitsjonbrell.com) for inspiration.

I want to add the following information on my card (the order of these, their size, and their casing is up to you):

Jon Brell
jon@HiItsJonBrell.com
@HiItsJonBrell
HiItsJonBrell.com
vidsharehub.example/HiItsJonBrell

I would also like to have somewhere on the card a small ad that says "Get a free course at https://HiItsJonBrell.com/FreeCourse". Feel free to play with that wording or layout if you need. I would prefer this text to be at the bottom of the card and subtle. Some small eye-catching thing might be ok but nothing huge or garish.

I plan on printing this card at pressquill.example (https://www.pressquill.example/us/design-guidelines/business-cards.html). I would like it to be the standard size (3.66" x 2.16"). I would prefer rounded corners and horizontal orientation. This is a two-side design. I would prefer the side with all of the information be primarily white but I like color text (again, flexible on that). On the front side, I like simple. Maybe just HiItsJonBrell.com (casing on that is up to you - whatever looks and reads the best - that goes for all of the casing). As for font choices, I prefer a modern, clean font. For example, Open Sans Light can be a nice option.

Website Info (might be helpful for the card):
Color Palette

Darkest blue - #263246
Alternate blue - #2F4E6A
Light blue - #2A98C3
Orange - #FF6201
White - #FFFFFF

Font for Jon Brell Logo

Jellyka Estryas Handwriting
http://www.typecrate.example/jellyka_estryas_handwriting.font

Fonts for Site Content and VidShare Thumbnails

Lovelo (bold title font)
http://www.glyphmill.example/lovelo-font/

Open Sans (body font)
http://www.letterbarn.example/fonts/open-sans

Industry/Entity Type

Software Development

Contact Information for Business Card

Jon Brell
jon@HiItsJonBrell.com
@HiItsJonBrell
HiItsJonBrell.com
vidsharehub.example/HiItsJonBrell

Get a free course at https://HiItsJonBrell.com/FreeCourse

Colors

Designer to choose colors to be used in the design.

Requirements
Nice to have
• Modern color - maybe primarily a color on the front and then that color as an accent on the back.
Should not have
• Lots of colors - I LOVE color but do not want a rainbow of colors on the card.

```html
<!DOCTYPE html>
<html lang="en">
<head>
<meta charset="utf-8">
<title>HiItsJonBrell.com — Business Card</title>
<link rel="stylesheet" href="https://fonts.googleapis.com/css2?family=Open+Sans:wght@700&family=Montserrat:wght@400&display=swap">
<style>
  :root {
    --stage: #cbcdcb;
    --blue-deep: #2473b6;
    --blue-light: #2a98c3;
    --blue-dark: #1d5a8c;
    --blue-mid: #3d9ad4;
    --white: #ffffff;
    --ink: #4f5257;
    --orange: #f26322;
  }
  * { margin: 0; padding: 0; box-sizing: border-box; }
  html, body { width: 1200px; height: 1200px; overflow: hidden; }
  body { background: var(--stage); position: relative; font-family: "Montserrat", sans-serif; }

  .card { position: absolute; left: 116px; width: 968px; }

  .card-front {
    top: 22px; height: 570px;
    background: linear-gradient(160deg, var(--blue-deep) 0%, #2580bd 50%, #2193c4 100%);
    border: 2px solid var(--white);
    display: flex; align-items: center; justify-content: center;
  }
  .front-domain {
    font-family: "Open Sans", sans-serif;
    font-weight: 700;
    font-size: 35px;
    color: var(--white);
    letter-spacing: -0.3px;
    margin-top: -140px;
  }

  .card-back { top: 595px; height: 571px; background: var(--white); }

  .geo-field {
    position: absolute; left: 0; top: 2px; width: 410px; height: 306px;
    background: linear-gradient(135deg, var(--blue-mid) 0%, var(--blue-deep) 50%, var(--blue-dark) 100%);
    opacity: 0.9;
  }

  .signature {
    position: absolute; left: 594px; top: 57px; width: 322px; height: 128px;
    background: linear-gradient(90deg, rgba(42,152,195,0.18), rgba(42,152,195,0.32));
    border-radius: 8px;
  }

  .contact-list { position: absolute; left: 0; top: 0; width: 100%; height: 100%; list-style: none; }
  .contact-item {
    position: absolute; right: 50px; height: 30px;
    display: flex; align-items: center; gap: 16px;
    font-size: 24px; color: var(--ink); white-space: nowrap;
  }
  .contact-item:nth-child(1) { top: 255px; }
  .contact-item:nth-child(2) { top: 292px; }
  .contact-item:nth-child(3) { top: 329px; }
  .contact-item:nth-child(4) { top: 367px; }
  .contact-icon { width: 30px; height: 26px; flex: none; }

  .promo {
    position: absolute; right: 50px; top: 503px;
    font-size: 19px; color: var(--orange); white-space: nowrap;
  }
</style>
</head>
<body>
  <section class="card card-front">
    <p class="front-domain">HiItsJonBrell.com</p>
  </section>

  <section class="card card-back">
    <div class="geo-field" role="img" aria-label="Geometric arrangement of blue triangles"></div>
    <div class="signature" role="img" aria-label="Handwritten signature: Jon Brell"></div>

    <ul class="contact-list">
      <li class="contact-item">
        <span>jon@HiItsJonBrell.com</span>
        <svg class="contact-icon" viewBox="0 0 30 26" aria-hidden="true">
          <rect x="1" y="3" width="28" height="21" rx="3" fill="#2a98c3"/>
          <path d="M3 6 L15 15 L27 6" fill="none" stroke="#fff" stroke-width="2.4"/>
        </svg>
      </li>
      <li class="contact-item">
        <span>@HiItsJonBrell</span>
        <svg class="contact-icon" viewBox="0 0 30 26" aria-hidden="true">
          <rect x="3" y="1" width="24" height="24" rx="4" fill="#2a98c3"/>
        </svg>
      </li>
      <li class="contact-item">
        <span>HiItsJonBrell.com</span>
        <svg class="contact-icon" viewBox="0 0 30 26" aria-hidden="true">
          <circle cx="15" cy="13" r="12" fill="#2a98c3"/>
          <ellipse cx="15" cy="13" rx="5" ry="12" fill="none" stroke="#fff" stroke-width="1.6"/>
          <line x1="3" y1="13" x2="27" y2="13" stroke="#fff" stroke-width="1.6"/>
        </svg>
      </li>
      <li class="contact-item">
        <span>vidsharehub.example/HiItsJonBrell</span>
        <svg class="contact-icon" viewBox="0 0 30 26" aria-hidden="true">
          <rect x="1" y="2" width="28" height="22" rx="4" fill="#2a98c3"/>
        </svg>
      </li>
    </ul>

    <p class="promo">Get a free course at: https://HiItsJonBrell.com/FreeCourse</p>
  </section>
</body>
</html>
```